Fresh easy to read restaurant menu

Burger Restaurant menu based on an island in Thailand. Light colours because we have dimmed lights and it needs to be easy to read. Need to fit on A3 size paper/ 2 sides. COULD BE LANDSCAPE POSITION TOO.
Colour choices around existing logo. Vintage fun look if possible. Owner needs to be able to change text when menu needs to change.
Have different major sections (Starters - Juicy burgers and sandwiches - Crunchy salads - Tasty meals - Sweet bites & desserts) smaller sections (Extras - Dips, mayos and more - Tumble's special thirst quenchers)
I uploaded my last menu design. I need a fresh look as we have used this last one for the past 4 years.
Please make sure it's not too dark and easy to read. LANDSCAPE is better. The menu items needs to the editable because we are located on a thai island and products are not always available. Prices needs constant changes too as we have low and high seasons.
Thanks for your time and effort.
Reason: Still looking for the right design. Some designers have committed but not enough time to submit designs.
Industry/Entity Type
Restaurant
Look and feel
Each slider illustrates characteristics of the customer's brand and the style your logo design should communicate.

```html
<!DOCTYPE html>
<html lang="en">
<head>
<meta charset="utf-8">
<title>Tumble's Restaurant &amp; Lounge – Menu</title>
<link href="https://fonts.googleapis.com/css2?family=Chewy&family=Kalam:wght@400;700&family=Open+Sans:wght@600;700&display=swap" rel="stylesheet">
<style>
  :root {
    --leaf-light: #dcedb8;
    --leaf: #c5e09a;
    --sand-light: #fcecae;
    --sand: #f7db86;
    --ink: #2a1d12;
    --orange: #ef7a2b;
    --orange-soft: #f3a56f;
    --brown: #7a3f1c;
    --white: #ffffff;
    --palm: #6fae3c;
  }
  * { box-sizing: border-box; margin: 0; padding: 0; }
  html, body { width: 1200px; height: 849px; overflow: hidden; background: #fff; }
  .menu { position: relative; width: 1200px; height: 849px; overflow: hidden; color: var(--ink); font-family: 'Open Sans', sans-serif; }
  .panel { position: absolute; top: 0; height: 849px; }
  .panel--left { left: 0; width: 598px; background: linear-gradient(180deg, var(--leaf-light), var(--leaf)); }
  .panel--right { left: 598px; width: 602px; background: linear-gradient(180deg, var(--sand-light), var(--sand)); }

  .art { position: absolute; border-radius: 12px; z-index: 1; }
  .art--palm { background: linear-gradient(180deg, #8cc04f, var(--palm)); }
  .art--coconut { background: radial-gradient(circle, #a36b35, #5d8f2c); border-radius: 50%; }
  .art--food { background: radial-gradient(circle, #f2c46a, #c0502a); border-radius: 50%; }
  .art--fries { background: linear-gradient(180deg, #f7c948, #d8407a); }
  .art--leaves { background: linear-gradient(0deg, #4f9a34, rgba(111,174,60,0)); border-radius: 0; }

  .brand { position: absolute; left: 190px; top: 64px; z-index: 2; font-family: 'Chewy', 'Kalam', cursive; font-size: 72px; line-height: 1; color: var(--brown); }
  .brand-sub { position: absolute; left: 262px; top: 146px; z-index: 2; font-family: 'Kalam', cursive; font-size: 17px; color: var(--brown); }

  .section-title { position: absolute; z-index: 2; transform: translateX(-50%); white-space: nowrap; line-height: 1; font-family: 'Chewy', 'Kalam', cursive; font-weight: 400; font-size: 28px; letter-spacing: 0.5px; color: var(--orange);
    text-shadow: 2px 0 var(--white), -2px 0 var(--white), 0 2px var(--white), 0 -2px var(--white), 2px 2px var(--white), -2px -2px var(--white), 2px -2px var(--white), -2px 2px var(--white), 3px 4px 0 rgba(90,40,10,.4); }
  .sub-title { position: absolute; z-index: 2; transform: translateX(-50%); white-space: nowrap; line-height: 1; font-family: 'Chewy', 'Kalam', cursive; font-weight: 400; font-size: 18px; color: var(--orange); letter-spacing: 1px; }
  .tagline { position: absolute; left: 902px; transform: translateX(-50%); white-space: nowrap; font-family: 'Kalam', cursive; font-size: 14px; }
  .pricing { position: absolute; left: 902px; transform: translateX(-50%); white-space: nowrap; font-weight: 700; font-size: 16px; }

  .item { position: absolute; z-index: 2; width: 533px; display: flex; align-items: baseline; white-space: nowrap; }
  .item--left { left: 34px; }
  .item--right { left: 633px; }
  .item__name { font-weight: 700; font-size: 15.5px; }
  .item__desc { font-family: 'Kalam', cursive; font-size: 14px; margin-left: 4px; }
  .item__price { margin-left: auto; font-weight: 700; font-size: 16px; }
  .note { position: absolute; z-index: 2; font-family: 'Kalam', cursive; font-size: 13.5px; white-space: nowrap; }
  .note--left { left: 34px; }
  .note--right { left: 633px; }

  .sauce-box { position: absolute; left: 632px; top: 403px; width: 537px; height: 111px; background: var(--orange-soft); border: 3px solid var(--white); border-radius: 10px; box-shadow: 0 0 0 1.5px #b4622f; }
  .sauce { position: absolute; font-family: 'Kalam', cursive; font-weight: 700; font-size: 15px; white-space: nowrap; }
</style>
</head>
<body>
<main class="menu">
  <section class="panel panel--left"></section>
  <section class="panel panel--right"></section>

  <!-- Left panel -->
  <div class="art art--palm" style="left:36px;top:24px;width:125px;height:150px" role="img" aria-label="Palm trees illustration"></div>
  <div class="brand">Tumble's</div>
  <div class="brand-sub">restaurant &amp; lounge</div>
  <div class="art art--coconut" style="left:474px;top:97px;width:82px;height:82px" role="img" aria-label="Coconut drink with tropical leaves"></div>

  <div class="art art--food" style="left:440px;top:200px;width:88px;height:62px" role="img" aria-label="Fresh salad vegetables"></div>
  <h2 class="section-title" style="left:297px;top:214px">CRUNCHY SALAD</h2>

  <div class="item item--left" style="top:251px"><span class="item__name">The Tuna</span><span class="item__desc">- Veggies, egg &amp; tuna with creamy dressing</span><span class="item__price">180</span></div>
  <div class="item item--left" style="top:282px"><span class="item__name">The Greek</span><span class="item__desc">- Lettuce, tomatoes, cucumbers, onions, olives &amp; feta cheese</span><span class="item__price">170</span></div>
  <div class="item item--left" style="top:314px"><span class="item__name">The Cesar</span><span class="item__desc">- Veggies, croutons, cheese, egg &amp; bacon</span><span class="item__price">180</span></div>
  <p class="note note--left" style="top:336px">Extra Chicken Breast ................. 50</p>
  <p class="note note--left" style="top:358px">Extra Smoked Salmon ................. 60</p>
  <div class="item item--left" style="top:389px"><span class="item__name">The Med</span><span class="item__desc">- <em>Chicken or Tuna</em> - Veggies, feta, olives &amp; hummus</span><span class="item__price">200</span></div>
  <div class="item item--left" style="top:420px"><span class="item__name">The Cob</span><span class="item__desc">- Veggies, chicken, bacon, blue cheese &amp; egg</span><span class="item__price">200</span></div>

  <div class="art art--fries" style="left:458px;top:494px;width:62px;height:74px" role="img" aria-label="Box of fries illustration"></div>
  <h2 class="section-title" style="left:297px;top:470px">HUNGER MANAGEMENT</h2>

  <div class="item item--left" style="top:506px"><span class="item__name">Homemade Fries</span><span class="item__price">70</span></div>
  <div class="item item--left" style="top:538px"><span class="item__name">Battered Onion bunch with dip</span><span class="item__price">100</span></div>
  <div class="item item--left" style="top:569px"><span class="item__name">Indian Roasted Chickpeas</span><span class="item__desc">- A low fat and nutritious beer snack!</span><span class="item__price">60</span></div>
  <div class="item item--left" style="top:601px"><span class="item__name">Crispy Raviolis</span><span class="item__desc">- Served with Marinara Sauce</span><span class="item__price">90</span></div>
  <div class="item item--left" style="top:632px"><span class="item__name">Yummy Hummus</span><span class="item__desc">- Served with Cracker &amp; Veggies</span><span class="item__price">120</span></div>
  <div class="item item--left" style="top:664px"><span class="item__name">Hummus Plate</span><span class="item__desc">- Meal size portion with a choice of one topping:</span><span class="item__price">180</span></div>
  <p class="note note--left" style="top:688px">Feta, chicken, bacon, olives, jalapenos, mushrooms, fried onions or</p>
  <p class="note note--left" style="top:711px">roasted chickpeas. Served with crackers &amp; veggies</p>
  <div class="item item--left" style="top:740px"><span class="item__name">Smoked Salmon Starter</span><span class="item__desc">- Served on cucumber slices with dill cream cheese</span><span class="item__price">140</span></div>
  <div class="item item--left" style="top:771px"><span class="item__name">Chicken Wings</span><span class="item__desc">(Regular or Super Spicy)</span><span class="item__price">130</span></div>
  <p class="note note--left" style="top:794px">Extra Blue Cheese Dip ................. 30</p>
  <div class="art art--leaves" style="left:0;top:815px;width:598px;height:34px" role="img" aria-label="Tropical leaves border"></div>

  <!-- Right panel -->
  <div class="art art--palm" style="left:1017px;top:0;width:183px;height:109px;border-radius:0 0 0 60px" role="img" aria-label="Palm leaves illustration"></div>
  <h2 class="section-title" style="left:896px;top:53px">HUNGER MANAGEMENT</h2>
  <div class="art art--food" style="left:995px;top:96px;width:92px;height:54px" role="img" aria-label="Plate of garlic bread and fries"></div>

  <div class="item item--right" style="top:100px"><span class="item__name">Garlic Bread</span><span class="item__price">80</span></div>
  <p class="note note--right" style="top:123px">Extra Cheese ................. 40</p>
  <div class="item item--right" style="top:152px"><span class="item__name">Warm Cheese Dip</span><span class="item__desc">- Served with baked tortilla chips</span><span class="item__price">150</span></div>
  <div class="item item--right" style="top:184px"><span class="item__name">Poutine</span><span class="item__desc">- French fries, gravy &amp; cheese...</span><span class="item__price">130</span></div>
  <p class="note note--right" style="top:209px">The most popular munchies from Québec, Canada!</p>
  <p class="note note--right" style="top:231px">Extra minced beef ................. 60</p>
  <p class="note note--right" style="top:253px">Extra pulled pork, chicken or bacon ................. 50</p>
  <p class="note note--right" style="top:275px">Mexican Style ................. 50 (jalapenos, onions, tomatoes and sour cream)</p>

  <h3 class="sub-title" style="left:902px;top:319px">MAYO, DIPS &amp; MORE</h3>
  <p class="tagline" style="top:343px">Pimp up your Fries and Burgers with our tasty Homemade Sauces</p>
  <p class="pricing" style="top:368px">SINGLE - 30 | DUO - 50 | TRIO - 70</p>

  <div class="sauce-box"></div>
  <p class="sauce" style="left:642px;top:410px">Chili Mayo</p>
  <p class="sauce" style="left:642px;top:436px">Garlic Mayo</p>
  <p class="sauce" style="left:642px;top:461px">Ranch Mayo</p>
  <p class="sauce" style="left:642px;top:487px">Honey Mustard Mayo</p>
  <p class="sauce" style="left:832px;top:410px">Sweet BBQ Sauce</p>
  <p class="sauce" style="left:832px;top:436px">Blue Cheese Dip</p>
  <p class="sauce" style="left:832px;top:461px">Thousand Island Dressing</p>
  <p class="sauce" style="left:832px;top:487px">Hummus</p>
  <p class="sauce" style="left:1047px;top:410px">Gravy</p>
  <p class="sauce" style="left:1047px;top:436px">Marinara Sauce</p>
  <p class="sauce" style="left:1047px;top:461px">Sour Cream</p>
  <p class="sauce" style="left:1047px;top:487px">Olive Tapenade</p>

  <div class="art art--food" style="left:1025px;top:533px;width:77px;height:62px" role="img" aria-label="Roast chicken meal illustration"></div>
  <h2 class="section-title" style="left:896px;top:555px">TASTY MEALS</h2>

  <div class="item item--right" style="top:591px"><span class="item__name">BBQ Palmwood Pork Ribs</span><span class="item__desc">- Served with fries &amp; coleslaw</span><span class="item__price">230</span></div>
  <div class="item item--right" style="top:621px"><span class="item__name">Hamburger Steak</span><span class="item__desc">- Two beef patties topped with fried onion and gravy</span><span class="item__price">220</span></div>
  <p class="note note--right" style="top:645px">Served with fries and salad</p>
  <div class="item item--right" style="top:674px"><span class="item__name">Macaroni &amp; Cheese</span><span class="item__price">160</span></div>
  <p class="note note--right" style="top:697px">Naacho Style ................. 60</p>
  <p class="note note--right" style="top:720px">(with minced beef, jalapenos, tomatoes &amp; sour cream)</p>
  <div class="item item--right" style="top:749px"><span class="item__name">Beef Kebab Wrap</span><span class="item__desc">- With sliced beef, hummus,</span><span class="item__price">200</span></div>
  <p class="note note--right" style="top:772px">Ranch mayo, veggies &amp; fresh coriander</p>
  <p class="note note--right" style="top:794px">Served with salad</p>
</main>
</body>
</html>
```